Advertising company unique advertising platform

we need a logo design for a new company based in Australia Melbourne. We develop innovated advertising platform where consumer can use this platform to get regular discount, as business owner they can use this platform for free advertisement. Payment for this advertisement platform only payable every two weeks, when I generate revenue for their business

Industry/Entity Type

Advertising

Contact Information for Business Card

Dale Pruitt | Co-Founder |Managing Director
Suite 718 263 Harrowgate Row Melbourne Vic 3000

ABN 41 902 615 273
Tel: +61 0491 528 307 | Email: dale.pruitt@corvelaxtro.com

Font styles to use
Decorative
Script

Requirements
Must have
• Try few different design and some round corner business card
Should not have
• One round corner business card...try 4 different colour background not only black, make sure two side is designed. Be creative so imagine you are giving this to a client make sure has wow factor, if you can also try one design with engrave like all the logo, words look 3d feel
• The word Advertising Platform use attached file font

```html
<!DOCTYPE html>
<html lang="en">
<head>
<meta charset="utf-8">
<title>Corvela Xtro — Business Cards</title>
<link href="https://fonts.googleapis.com/css2?family=PT+Sans:ital,wght@0,400;0,700;1,400&display=swap" rel="stylesheet">
<style>
  :root {
    --stage: #8c8c8c;
    --ink-dark: #111111;
    --ink-light: #ffffff;
    --card-black: #000000;
    --card-white: #ffffff;
    --card-mint: #cff5f3;
    --card-cream: #fcefe0;
    --brand-orange: #f26a2e;
    --brand-teal: #2fd3c0;
    --icon-orange: #f07a2a;
  }
  * { box-sizing: border-box; margin: 0; padding: 0; }
  html, body { width: 977px; height: 1200px; overflow: hidden; }
  body {
    background: var(--stage);
    font-family: "PT Sans", Arial, sans-serif;
    position: relative;
  }
  .card {
    position: absolute;
    width: 420px;
    height: 232px;
    border-radius: 10px;
    overflow: hidden;
    color: var(--ink-dark);
  }
  .card--black { background: var(--card-black); color: var(--ink-light); }
  .card--white { background: var(--card-white); }
  .card--mint  { background: var(--card-mint); }
  .card--cream { background: var(--card-cream); }

  .front { left: 62px; }
  .back  { left: 492px; }
  .row-1 { top: 50px; }
  .row-2 { top: 329px; }
  .row-3 { top: 607px; }
  .row-4 { top: 886px; }

  .wordmark {
    position: absolute;
    display: flex;
    align-items: center;
    gap: 8px;
    font-size: 27px;
    font-weight: 700;
    color: var(--brand-orange);
    white-space: nowrap;
    line-height: 1;
  }
  .wordmark__dot {
    width: 24px; height: 24px;
    border-radius: 50%;
    background: var(--brand-teal);
    flex: none;
  }
  .back .wordmark { left: 50%; top: 50%; transform: translate(-50%, -50%); }

  .abn { position: absolute; font-size: 9px; }

  .holder { position: absolute; font-size: 9px; line-height: 12px; }
  .holder__name { font-size: 12px; font-weight: 700; line-height: 14px; }
  .card--black .holder__role { font-style: italic; }

  .contact { position: absolute; list-style: none; font-size: 9px; line-height: 12px; }
  .contact li { display: flex; align-items: flex-start; gap: 6px; margin-top: 8px; }
  .contact li:first-child { margin-top: 0; margin-bottom: -2px; }
  .contact svg { width: 9px; height: 9px; flex: none; margin-top: 1px; fill: var(--icon-orange); }
</style>
</head>
<body>
<svg width="0" height="0" style="position:absolute" aria-hidden="true">
  <defs>
    <symbol id="icon-pin" viewBox="0 0 10 10"><path d="M5 0a3.6 3.6 0 0 0-3.6 3.6C1.4 6.3 5 10 5 10s3.6-3.7 3.6-6.4A3.6 3.6 0 0 0 5 0zm0 5a1.4 1.4 0 1 1 0-2.8A1.4 1.4 0 0 1 5 5z"/></symbol>
    <symbol id="icon-phone" viewBox="0 0 10 10"><path d="M2.1 0.4l1.5 1.9-.9 1.3c.6 1.3 1.6 2.3 2.9 2.9l1.3-.9 1.9 1.5-.9 2C4.2 9 1 5.8.2 1.3z"/></symbol>
    <symbol id="icon-mail" viewBox="0 0 10 10"><rect x="0" y="1.5" width="10" height="7" rx="1"/><path d="M1 2.5l4 3 4-3" fill="none" stroke="#fff" stroke-width="0.9"/></symbol>
    <symbol id="icon-web" viewBox="0 0 10 10"><circle cx="5" cy="5" r="5"/><path d="M0.5 5h9M5 0.5c-2 2.5-2 6.5 0 9M5 0.5c2 2.5 2 6.5 0 9" fill="none" stroke="#fff" stroke-width="0.6"/></symbol>
  </defs>
</svg>

<!-- Black card -->
<section class="card card--black front row-1">
  <div class="wordmark" style="left:38px;top:68px"><span class="wordmark__dot"></span>Corvela Xtro</div>
  <div class="holder" style="left:93px;top:151px">
    <p class="holder__name">Dale Pruitt</p>
    <p class="holder__role">Co-Founder | Managing Director</p>
    <p class="holder__role">Founder &amp; Director</p>
  </div>
  <ul class="contact" style="left:255px;top:96px">
    <li><svg><use href="#icon-pin"/></svg><span>Suite 718 263<br>Harrowgate Row<br>Melbourne Vic 3000</span></li>
    <li><svg><use href="#icon-phone"/></svg><span>+61 0491 528 307</span></li>
    <li><svg><use href="#icon-mail"/></svg><span>dale.pruitt@corvelaxtro.com</span></li>
    <li><svg><use href="#icon-web"/></svg><span>www.corvelaxtro.com</span></li>
  </ul>
</section>
<section class="card card--black back row-1">
  <div class="wordmark"><span class="wordmark__dot"></span>Corvela Xtro</div>
</section>

<!-- White card -->
<section class="card card--white front row-2">
  <div class="wordmark" style="left:38px;top:62px"><span class="wordmark__dot"></span>Corvela Xtro</div>
  <p class="abn" style="left:98px;top:132px">ABN 41 902 615 273</p>
  <div class="holder" style="left:221px;top:43px">
    <p class="holder__name">Dale Pruitt</p>
    <p class="holder__role">Co-Founder | Managing Director</p>
    <p class="holder__role">Founder &amp; Director</p>
  </div>
  <ul class="contact" style="left:218px;top:96px">
    <li><svg><use href="#icon-pin"/></svg><span>Suite 718 263<br>Harrowgate Row<br>Melbourne Vic 3000</span></li>
    <li><svg><use href="#icon-phone"/></svg><span>+61 0491 528 307</span></li>
    <li><svg><use href="#icon-mail"/></svg><span>dale.pruitt@corvelaxtro.com</span></li>
    <li><svg><use href="#icon-web"/></svg><span>www.corvelaxtro.com</span></li>
  </ul>
</section>
<section class="card card--white back row-2">
  <div class="wordmark"><span class="wordmark__dot"></span>Corvela Xtro</div>
</section>

<!-- Mint card -->
<section class="card card--mint front row-3">
  <div class="wordmark" style="left:215px;top:64px"><span class="wordmark__dot"></span>Corvela Xtro</div>
  <p class="abn" style="left:252px;top:143px">ABN 41 902 615 273</p>
  <div class="holder" style="left:248px;top:162px">
    <p class="holder__name">Dale Pruitt</p>
    <p class="holder__role">Co-Founder | Managing Director</p>
    <p class="holder__role">Founder &amp; Director</p>
  </div>
  <ul class="contact" style="left:65px;top:104px">
    <li><svg><use href="#icon-pin"/></svg><span>Suite 718 263<br>Harrowgate Row<br>Melbourne Vic 3000</span></li>
    <li><svg><use href="#icon-phone"/></svg><span>+61 0491 528 307</span></li>
    <li><svg><use href="#icon-mail"/></svg><span>dale.pruitt@corvelaxtro.com</span></li>
    <li><svg><use href="#icon-web"/></svg><span>www.corvelaxtro.com</span></li>
  </ul>
</section>
<section class="card card--mint back row-3">
  <div class="wordmark"><span class="wordmark__dot"></span>Corvela Xtro</div>
</section>

<!-- Cream card -->
<section class="card card--cream front row-4">
  <div class="wordmark" style="left:38px;top:64px"><span class="wordmark__dot"></span>Corvela Xtro</div>
  <p class="abn" style="left:98px;top:133px">ABN 41 902 615 273</p>
  <div class="holder" style="left:93px;top:151px">
    <p class="holder__name">Dale Pruitt</p>
    <p class="holder__role">Co-Founder | Managing Director</p>
    <p class="holder__role">Founder &amp; Director</p>
  </div>
  <ul class="contact" style="left:255px;top:96px">
    <li><svg><use href="#icon-pin"/></svg><span>Suite 718 263<br>Harrowgate Row<br>Melbourne Vic 3000</span></li>
    <li><svg><use href="#icon-phone"/></svg><span>+61 0491 528 307</span></li>
    <li><svg><use href="#icon-mail"/></svg><span>dale.pruitt@corvelaxtro.com</span></li>
    <li><svg><use href="#icon-web"/></svg><span>www.corvelaxtro.com</span></li>
  </ul>
</section>
<section class="card card--cream back row-4">
  <div class="wordmark"><span class="wordmark__dot"></span>Corvela Xtro</div>
</section>
</body>
</html>
```